Meridian Cataract Surgery and Cosmetic Eyelid Surgery

We need Three page website design (home page and interior page template with two looks) with accompanying CSS code. 1. Home page, 2. General Eye-Care page, 3. Cosmetic Eyelid Surgery. #2 an #3 would be only slightly different. See below.

The site being redesigned is http://www.brightlume-vision.com.

The content will remain consistent with the current site.

Additional graphics will be included, especially a number of "Before and after" photos of patients for the various procedures.

You can see competitive sites here: http://www.findora.net/search?q=cosmetic+eyelid+surgury+santa+rosa&ie=utf-8&oe=utf-8&aq=t&client=browser-b&rlz=1R1KKMM_en___US384

The client likes http://www.optiwell-pmc.com, which has a serious look he likes (not necessarily the colors or design). Avoid too many "happy loving couples" and pretty women, on the main page or cataract/general eye-care pages. They are, however, good on the cosmetic pages.

When patients look at the *cosmetic surgery* pages, they can see the pretty women/couples. For *eye surgery* (which is what this is all about) they should see an attractive, active OLDER couple(s) on cataract surgery and refractive surgery pages.

In the US, premium IOL (Intraocular lens - a clear plastic lens that is implanted in the eye; usually done when the natural lens has been removed in a cataract operation) cataract surgery, cosmetic and refractive surgery are not fully paid for by insurance, so patients can afford to pay for it themselves and are more well-off than the normal market.
Updates

Do not use the graphics or look and feel of the current site.  We are looking for a NEW design, not a remix of the old elements.

The new logo is at http://www.pitchforge.net/file.aspx?fileLocation=meridianoptilogo0.jpg

 
Do NOT use the old logo.  If your submitted design uses the old logo, please fix it and delete the one with the old logo.

Sorry for not making this clearer when we started.

Normal 0 false false false EN-US X-NONE X-NONE I want to see a home page that gives equal billing to general eyecare and cosmetic and RECONSTRUCTIVE eyelid surgery.   General eyecare should be listed first.  This should have the correct Practice name and Logo:   Meridian Optical and Cosmetic Eyelid Surgery Center.  The home page should be inviting to both old and young, men and women.  The General eyecare page should have similar appeal.  Cosmetic Page should be decidedly more feminine.  The home page should also highlight Dr. Brennet' s qualification and provide a site map/navigation.

The colors of the logo do not need to be limited to black and white.  The logos MUST be integrated into the design, not just pasted on the page.

Read the brief carefully and pay careful attention to the target markets.

 

Reason: Designs are headed in the right direction, but need more refining.

vector art uploaded:  logo.ai

Reason: Still considering.

Target Market(s)

OLDER men and women. People whose faces, eyes, etc., have an aged look that they want to look younger. ALSO patients who want to have the best possible vision after CATARACT SURGERY. Patients who want Premium IOL'S which give them vision at both distance and near WITHOUT GLASSES. STATE OF THE ART GLAUCOMA SURGERY.

Industry/Entity Type

Plastic

Requirements
Must have
• Easy to read. Some readers may have vision difficulties. Easy to navigate for the elderly market. Cosmetic page may be a little more complex.

```html
<!DOCTYPE html>
<html lang="en">
<head>
<meta charset="utf-8">
<title>Meridian Optical – Cosmetic Eyelid Surgery Center</title>
<link href="https://fonts.googleapis.com/css2?family=Questrial&family=Arimo:wght@400;700&display=swap" rel="stylesheet">
<style>
:root{
  --navy:#0a2a8a;
  --navy-deep:#031f78;
  --royal:#1640b8;
  --sky:#1a7fc4;
  --page-gray:#d6d6d6;
  --panel-gray:#d3d3d3;
  --ink:#111;
  --muted:#8a8a8a;
  --white:#fff;
}
*{margin:0;padding:0;box-sizing:border-box}
html,body{width:1161px;height:1200px;overflow:hidden}
body{position:relative;background:var(--page-gray);font-family:"Arimo",Arial,sans-serif;color:var(--ink)}
.heading{font-family:"Questrial",sans-serif}

.site-header{position:absolute;left:0;top:0;width:1161px;height:121px;background:linear-gradient(#fff,#e9e9ee)}
.brand{position:absolute;left:148px;top:30px;display:flex;align-items:center;gap:12px}
.brand-dot{width:34px;height:34px;border-radius:50%;background:var(--navy)}
.brand-name{font-family:"Questrial",sans-serif;font-size:40px;color:var(--navy);letter-spacing:1px}
.doctor-contact{position:absolute;right:134px;top:45px;text-align:right;color:var(--navy)}
.doctor-name{font-size:16px}
.call-line{font-size:13px;margin-top:9px}
.call-line span{font-size:17px}

.main-nav{position:absolute;left:0;top:121px;width:1161px;height:42px;background:linear-gradient(var(--royal),var(--navy-deep));border-top:1px solid #6a86d8;border-bottom:1px solid #6a86d8}
.main-nav ul{list-style:none;display:flex;position:absolute;left:150px;top:0;height:40px;align-items:center;font-family:"Questrial",sans-serif;font-size:16.5px;color:#fff}
.main-nav li{padding:0 6px}
.main-nav li.current{background:#0d2f9a;height:40px;line-height:40px;padding:0 14px;margin-right:4px}
.main-nav .sep{padding:0}

.hero-band{position:absolute;left:0;top:163px;width:1161px;height:280px;background:linear-gradient(160deg,#0a2790 0%,#1d56c8 40%,#0a2a90 70%,#2a6ad8 100%)}
.hero{position:absolute;left:150px;top:163px;width:877px;height:280px;background:#fff;overflow:hidden}
.hero-photo{position:absolute;left:380px;top:0;width:497px;height:280px;background:linear-gradient(90deg,#f1f1f1 0%,#d9c2b0 35%,#e7cdb6 65%,#c9a77d 100%)}
.hero-copy{position:absolute;left:14px;top:10px;width:370px}
.hero-title{font-size:24px;line-height:27.5px;color:var(--navy)}
.hero-text{font-size:10.5px;line-height:16.5px;color:var(--muted);margin-top:10px}
.slide-pager{position:absolute;left:17px;top:209px;display:flex;gap:6px}
.slide-pager span{width:13px;height:13px;border:1px solid #999;background:#fff;font-size:10px;line-height:11px;text-align:center;color:#333}
.slide-pager span.active{color:var(--sky);border-color:var(--sky)}

.content{position:absolute;left:150px;top:443px;width:877px;height:526px;background:#fff}
.intro{position:absolute;left:26px;top:12px;width:540px}
.page-title{font-size:30px;color:var(--navy);letter-spacing:.5px}
.section-title{font-size:18px;color:var(--navy);margin-top:14px}
.body-copy{font-size:11px;line-height:16.5px;margin-top:2px}
.body-copy + .body-copy{margin-top:16px}
.link-list{list-style:none;margin-top:24px}
.link-list li{font-family:"Questrial",sans-serif;font-size:14.5px;color:var(--navy);margin-bottom:8px;display:flex;align-items:center;gap:6px}
.procedure h3{font-family:"Questrial",sans-serif;font-weight:400;font-size:14px;color:var(--navy);margin-top:7px}
.procedure p{font-size:11px;line-height:16.5px}

.contact-panel{position:absolute;left:805px;top:455px;width:209px;height:248px;background:var(--panel-gray);border:1px solid #b5b5b5}
.contact-title{font-size:19px;color:var(--sky);position:absolute;left:21px;top:9px}
.field{position:absolute;left:21px;width:165px;height:25px;background:#fff;border:1px solid var(--sky);border-radius:2px;font-size:10.5px;color:var(--sky);padding:7px 8px}
.field.message{height:89px}

.office-map{position:absolute;left:824px;top:743px;width:160px}
.map-link{font-size:17px;color:var(--navy);text-decoration:underline;text-align:center}
.map-thumb{margin:13px auto 0;width:160px;height:120px;border:1px solid #ccc;background:linear-gradient(135deg,#cfe0e8,#efe6d4 50%,#e3d2be)}
.address{font-size:10.5px;line-height:16.5px;text-align:center;margin-top:10px;width:186px;margin-left:-13px}

.site-footer{position:absolute;left:0;top:969px;width:1161px;height:193px;background:linear-gradient(170deg,#0a2a8a,#0d36a6 50%,#082478)}
.footer-col{position:absolute;top:10px;color:#fff}
.footer-col h4{font-family:"Questrial",sans-serif;font-weight:400;font-size:14.5px;line-height:17px;height:42px}
.footer-col h4.linked{text-decoration:underline}
.footer-col ul{list-style:none;width:133px;border-top:1px solid #c8d2f0}
.footer-col li{font-size:12px;height:24px;line-height:23px;border-bottom:1px solid #c8d2f0;padding-left:14px;position:relative}
.footer-col li::before{content:"";position:absolute;left:5px;top:10px;width:3px;height:3px;border-radius:50%;background:#fff}
.copyright{position:absolute;left:0;top:1162px;width:1161px;height:38px;background:linear-gradient(#1645c0,#0a2a8a);color:#fff;font-size:11px;text-align:center;line-height:40px;border-top:1px solid #3c66d4}
</style>
</head>
<body>

<header class="site-header">
  <div class="brand"><div class="brand-dot"></div><div class="brand-name">Meridian Optical</div></div>
  <div class="doctor-contact">
    <div class="doctor-name">Martin L. Brennet M.D.</div>
    <div class="call-line">Call Now : <span>707-555-0182</span></div>
  </div>
</header>

<nav class="main-nav">
  <ul>
    <li class="current">Home</li>
    <li>Diabetic Retinopathy</li><li class="sep">|</li>
    <li>Flashes and Floaters</li><li class="sep">|</li>
    <li>Glaucoma</li><li class="sep">|</li>
    <li>Macular Degeneration</li><li class="sep">|</li>
    <li>Refractive Surgery</li>
  </ul>
</nav>

<div class="hero-band" role="img" aria-label="Blue abstract light-swoosh background"></div>
<section class="hero">
  <div class="hero-photo" role="img" aria-label="Photo of two smiling young women"></div>
  <div class="hero-copy">
    <h1 class="hero-title heading" style="font-weight:400">Welcome to Meridian Optical Eye Care and the Aesthetic Surgery Center.</h1>
    <p class="hero-text">Dr Brennet specializes in cosmetic and reconstructive laser surgery of the eyelids and upper face. Because he performs the procedures with super-pulsed carbon dioxide lasers, his patients enjoy less bruising and swelling and are back to work (or play) sooner.</p>
  </div>
  <div class="slide-pager"><span class="active">1</span><span>2</span><span>3</span></div>
</section>

<main class="content">
  <div class="intro">
    <h1 class="page-title heading" style="font-weight:400">Welcome to Our Website</h1>
    <h2 class="section-title heading" style="font-weight:400">Eyelid and Facial Cosmetic Surgery</h2>
    <p class="body-copy">Dr Brennet specializes in cosmetic and reconstructive laser surgery of the eyelids and upper face. Because he performs the procedures with super-pulsed carbon dioxide lasers, his patients enjoy less bruising and swelling and are back to work (or play) sooner.</p>
    <p class="body-copy">Dr. Brennet is one of an elite rank of 400 surgeons nationally who are trained in the reconstruction and beautification of eyelids. Following his residency in Ophthalmology, Dr. Brennet was awarded a formal fellowship in eyelid plastic and orbital surgery (One of only 30 nationwide). Is cosmetic eyelid or facial plastic surgery right for you? Enter here to learn more about how cosmetic eyelid surgery can help you.</p>
    <ul class="link-list">
      <li><svg width="12" height="10" viewBox="0 0 12 10"><path d="M0 0 12 5 0 10 3 5z" fill="#1a7fc4"/></svg>Cosmetic Eyelid Surgery For Men and Women</li>
      <li><svg width="12" height="10" viewBox="0 0 12 10"><path d="M0 0 12 5 0 10 3 5z" fill="#1a7fc4"/></svg>How Aesthetic Eyelid Surgery is Performed</li>
    </ul>
    <div class="procedure"><h3>Upper Eyelids:</h3><p>Advanced laser eyelid surgery precisely removes bulges and wrinkles and allows for less bruising and faster recuperation.</p></div>
    <div class="procedure"><h3>Lower Eyelids:</h3><p>Advanced laser eyelid surgery precisely removes bulges and wrinkles and allows for less bruising and faster recuperation.</p></div>
    <div class="procedure"><h3>Forehead/Brow:</h3><p>Endoscopic Brow Lift improves brow/forehead position and contour with only small incisions.</p></div>
    <div class="procedure"><h3>Laser Skin Resurfacing:</h3><p>Deal for removing wrinkles around the eyes and mouth. Your complexion looks years younger!.</p></div>
  </div>
</main>

<aside class="contact-panel">
  <h2 class="contact-title heading" style="font-weight:400">Contact Us</h2>
  <div class="field" style="top:40px">Name:</div>
  <div class="field" style="top:68px">Phone :</div>
  <div class="field" style="top:96px">Email:</div>
  <div class="field message" style="top:124px">Message:</div>
</aside>

<aside class="office-map">
  <div class="map-link">Map to Our Office</div>
  <div class="map-thumb" role="img" aria-label="Street map showing the office location"></div>
  <p class="address">Martin L. Brennet M.D., 412<br>Alder Street, Santa Rosa, CA<br>(877)-555-0139</p>
</aside>

<footer class="site-footer">
  <div class="footer-col" style="left:180px"><h4 class="linked">How Aesthetic Eyelid<br>Surgery is Performed.</h4>
    <ul><li>Home</li><li>About Us</li><li>Portfolio</li><li>Our Services</li><li>Contact Us</li></ul></div>
  <div class="footer-col" style="left:405px"><h4 class="linked">General Ophthalmology</h4>
    <ul><li>Home</li><li>About Us</li><li>Portfolio</li><li>Our Services</li><li>Contact Us</li></ul></div>
  <div class="footer-col" style="left:627px"><h4>About Dr. Martin Brennet</h4>
    <ul><li>Home</li><li>About Us</li><li>Portfolio</li><li>Our Services</li><li>Contact Us</li></ul></div>
  <div class="footer-col" style="left:841px"><h4>About Dr. Martin Brennet</h4>
    <ul><li>Home</li><li>About Us</li><li>Portfolio</li><li>Our Services</li><li>Contact Us</li></ul></div>
</footer>
<div class="copyright">Copyright © 2011 MeridianOpticalCare.com</div>

</body>
</html>
```